| 希望する色 | 黄系 |
【 概要 】 PAKUのリッチの制作をお願いします。 ほぼデザインを出来ているのでデータへの落し込みと多少のブラッシュアップをお願い出来ればと思います。 【 依頼内容 】 添付した画像のように1枚の画像に6分割したリッチメニューになります。 ファイル形式:JPG、JPEG、PNG ファイルサイズ:1MB以下 画像サイズ:2500px × 1686px 【 提供素材 】 ・添付ファイルよりご確認下さい。 【 デザインイメージ 】 ・シンプル ・ピクトグラン ・こちらのサイトのPAKUアカウントで使用します https://morizuto.jp/ 良ければ友達追加をしてイメージ頂けますと幸いです。 <a href="https://tsu.ee/Q8pW2RZ"><img src="https://cdn.paku-assets.example/n/paku_add_friends/btn/ja.png" alt="友だち追加" height="36" border="0"></a> ご質問がありましたら、気軽にお問い合わせください。 応募をお待ちしております! |
| 参考記事URL | ||
| https://morizuto.jp/ | ||
どれも素敵なご提案を頂いたのですが一番動線を考えられた作品を選ばせて頂きました。
色々なご提案を頂いたのにお選び出来ずに申し訳ございません。
また色々と今後もお願いをする計画がございますのでぜひ次回もご参画を頂けますと幸いです。

```html
<!DOCTYPE html>
<html lang="ja">
<head>
<meta charset="utf-8">
<title>ステップメニュー</title>
<link rel="stylesheet" href="https://fonts.googleapis.com/css2?family=M+PLUS+Rounded+1c:wght@700;800&display=swap">
<style>
  :root {
    --bg-yellow: #fde84a;
    --stripe-yellow: #fff39c;
    --ink: #231f20;
    --orange: #f4a339;
    --card: #ffffff;
  }
  * { box-sizing: border-box; margin: 0; padding: 0; }
  html, body { width: 1200px; height: 810px; overflow: hidden; }
  body {
    font-family: "M PLUS Rounded 1c", sans-serif;
    background: repeating-linear-gradient(-45deg,
      var(--bg-yellow) 0 34px, var(--stripe-yellow) 34px 52px);
    position: relative;
  }
  .step {
    position: absolute;
    width: 356px;
    height: 348px;
  }
  .step-card {
    position: absolute;
    inset: 0;
    background: var(--card);
    border: 6px solid var(--ink);
    border-radius: 14px;
  }
  .step-tag {
    position: absolute;
    left: -14px;
    top: -38px;
    width: 76px;
    text-align: center;
    z-index: 2;
  }
  .step-word {
    display: block;
    font-weight: 800;
    font-size: 24px;
    color: var(--ink);
    letter-spacing: 1px;
    line-height: 1;
    transform: rotate(-6deg);
    margin-bottom: 4px;
  }
  .step-num {
    display: flex;
    align-items: center;
    justify-content: center;
    width: 72px;
    height: 72px;
    border-radius: 50%;
    background: var(--orange);
    border: 4px solid var(--ink);
    font-weight: 800;
    font-size: 40px;
    color: var(--ink);
    margin: 0 auto;
  }
  .step-icon {
    position: absolute;
    left: 50%;
    top: 34px;
    transform: translateX(-50%);
    width: 240px;
    height: 190px;
  }
  .step-label {
    position: absolute;
    left: 10px;
    right: 10px;
    bottom: 12px;
    height: 78px;
    background: var(--orange);
    border-radius: 6px;
    display: flex;
    align-items: center;
    justify-content: center;
    font-weight: 800;
    font-size: 34px;
    line-height: 1;
    white-space: nowrap;
    overflow: hidden;
    color: var(--ink);
  }
  .step-label-long {
    font-size: 31px;
    letter-spacing: -1px;
  }
  .brand-name {
    position: absolute;
    right: 18px;
    top: 16px;
    font-weight: 800;
    font-size: 28px;
    color: var(--orange);
  }
  .col-1 { left: 22px; }
  .col-2 { left: 424px; }
  .col-3 { left: 826px; }
  .row-1 { top: 44px; }
  .row-2 { top: 448px; }
</style>
</head>
<body>

<section class="step col-1 row-1">
  <div class="step-card">
    <span class="brand-name">モリズト</span>
    <svg class="step-icon" viewBox="0 0 240 190" aria-label="空室を探す家と虫眼鏡のアイコン">
      <path d="M40 80 L110 30 L180 80 V170 H40 Z" fill="var(--orange)" transform="translate(-10 6)"/>
      <path d="M40 80 L110 30 L180 80 V170 H40 Z" fill="none" stroke="var(--ink)" stroke-width="12" stroke-linejoin="round"/>
      <circle cx="130" cy="120" r="30" fill="#fff" stroke="var(--ink)" stroke-width="10"/>
      <line x1="152" y1="142" x2="185" y2="175" stroke="var(--ink)" stroke-width="14" stroke-linecap="round"/>
    </svg>
    <div class="step-label">空室確認する</div>
  </div>
  <div class="step-tag"><span class="step-word">STEP</span><span class="step-num">1</span></div>
</section>

<section class="step col-2 row-1">
  <div class="step-card">
    <svg class="step-icon" viewBox="0 0 240 190" aria-label="カレンダーのアイコン">
      <rect x="40" y="30" width="160" height="145" rx="8" fill="#fff" stroke="var(--ink)" stroke-width="10"/>
      <rect x="40" y="30" width="160" height="28" fill="var(--ink)"/>
      <rect x="70" y="16" width="10" height="30" rx="4" fill="var(--ink)"/>
      <rect x="160" y="16" width="10" height="30" rx="4" fill="var(--ink)"/>
      <g fill="var(--ink)">
        <rect x="58" y="72" width="14" height="12"/><rect x="80" y="72" width="14" height="12"/><rect x="102" y="72" width="14" height="12"/><rect x="124" y="72" width="14" height="12"/><rect x="146" y="72" width="14" height="12"/>
        <rect x="58" y="94" width="14" height="12"/><rect x="80" y="94" width="14" height="12"/><rect x="102" y="94" width="14" height="12"/>
        <rect x="58" y="116" width="14" height="12"/><rect x="80" y="116" width="14" height="12"/><rect x="102" y="116" width="14" height="12"/><rect x="124" y="116" width="14" height="12"/><rect x="146" y="116" width="14" height="12"/>
        <rect x="58" y="138" width="14" height="12"/><rect x="80" y="138" width="14" height="12"/>
      </g>
      <rect x="124" y="92" width="92" height="18" fill="var(--orange)"/>
    </svg>
    <div class="step-label">内見予約する</div>
  </div>
  <div class="step-tag"><span class="step-word">STEP</span><span class="step-num">2</span></div>
</section>

<section class="step col-3 row-1">
  <div class="step-card">
    <svg class="step-icon" viewBox="0 0 240 190" aria-label="申込書とペンのアイコン">
      <rect x="60" y="20" width="120" height="155" rx="6" fill="#fff" stroke="var(--ink)" stroke-width="10"/>
      <circle cx="160" cy="110" r="30" fill="var(--orange)"/>
      <g stroke="var(--ink)" stroke-width="8" stroke-linecap="round">
        <line x1="82" y1="55" x2="158" y2="55"/><line x1="82" y1="80" x2="158" y2="80"/>
        <line x1="82" y1="105" x2="140" y2="105"/><line x1="82" y1="130" x2="130" y2="130"/>
      </g>
      <line x1="160" y1="112" x2="200" y2="152" stroke="var(--ink)" stroke-width="12" stroke-linecap="round"/>
    </svg>
    <div class="step-label">お申し込み</div>
  </div>
  <div class="step-tag"><span class="step-word">STEP</span><span class="step-num">3</span></div>
</section>

<section class="step col-1 row-2">
  <div class="step-card">
    <svg class="step-icon" viewBox="0 0 240 190" aria-label="トラックのアイコン">
      <rect x="100" y="40" width="105" height="100" fill="var(--orange)" transform="translate(-8 6)"/>
      <rect x="100" y="40" width="105" height="100" fill="none" stroke="var(--ink)" stroke-width="10"/>
      <path d="M30 150 V95 L50 70 H95 V150 Z" fill="var(--ink)"/>
      <rect x="30" y="140" width="178" height="14" fill="var(--ink)"/>
      <circle cx="62" cy="160" r="16" fill="var(--ink)"/>
      <circle cx="170" cy="160" r="16" fill="var(--ink)"/>
    </svg>
    <div class="step-label">引越の手配</div>
  </div>
  <div class="step-tag"><span class="step-word">STEP</span><span class="step-num">4</span></div>
</section>

<section class="step col-2 row-2">
  <div class="step-card">
    <svg class="step-icon" viewBox="0 0 240 190" aria-label="水道・電気・Wi-Fiのアイコン">
      <g fill="var(--ink)">
        <rect x="14" y="70" width="52" height="16" rx="4"/>
        <rect x="20" y="58" width="30" height="8" rx="3"/>
        <rect x="52" y="78" width="14" height="28"/>
        <path d="M59 120 q-10 16 0 22 q10 -6 0 -22 Z" fill="var(--orange)"/>
      </g>
      <circle cx="118" cy="100" r="24" fill="#fff" stroke="var(--ink)" stroke-width="8"/>
      <rect x="106" y="122" width="24" height="22" fill="var(--ink)"/>
      <text x="178" y="68" font-size="22" font-weight="800" fill="var(--ink)" text-anchor="middle" font-family="M PLUS Rounded 1c, sans-serif">Wi-Fi</text>
      <g fill="none" stroke="var(--ink)" stroke-width="8" stroke-linecap="round">
        <path d="M150 102 a40 40 0 0 1 56 0"/>
        <path d="M160 114 a26 26 0 0 1 36 0"/>
      </g>
      <circle cx="178" cy="128" r="6" fill="var(--orange)"/>
      <text x="186" y="176" font-size="22" font-weight="800" fill="var(--ink)" text-anchor="middle" font-family="M PLUS Rounded 1c, sans-serif">など</text>
    </svg>
    <div class="step-label step-label-long">ライフラインの手配</div>
  </div>
  <div class="step-tag"><span class="step-word">STEP</span><span class="step-num">5</span></div>
</section>

<section class="step col-3 row-2">
  <div class="step-card">
    <svg class="step-icon" viewBox="0 0 240 190" aria-label="鍵のアイコン">
      <g transform="rotate(35 120 95)">
        <rect x="70" y="38" width="60" height="66" rx="28" fill="var(--orange)" transform="translate(-8 6)"/>
        <rect x="70" y="38" width="60" height="66" rx="28" fill="#fff" stroke="var(--ink)" stroke-width="10"/>
        <rect x="90" y="56" width="20" height="12" rx="6" fill="var(--ink)"/>
        <path d="M92 104 V178 H108 V168 H120 V156 H108 V146 H118 V134 H108 V104" fill="#fff" stroke="var(--ink)" stroke-width="9" stroke-linejoin="round"/>
      </g>
    </svg>
    <div class="step-label">鍵の受け渡し</div>
  </div>
  <div class="step-tag"><span class="step-word">STEP</span><span class="step-num">6</span></div>
</section>

</body>
</html>
```